New Business Card for General Contractor Marketing

Need a business card the is more like a marketing promotion of our services
Must be horizontal orientation, One Sided Only, Max font size, Organize the Services
#1 General Contractor for Realtors
Remodels – Renovations – Repairs
Water & Mold Damage Experts
Painting: Interior/ Exterior
Flooring: Wood / LVT / Carpet
Plumbing: Repairs & Upgrades
Electric: Lights & Energy Efficient Upgrades
Kitchen & Bath Remodels
Fast Inspections Repair Billed Thru Escrow
BrightHarborBuilds.com
555-418-2796

Industry/Entity Type

General Contractor

Contact Information for Business Card

One Sided Only: #1 General Contractor for Realtors Remodels – Renovations – Repairs Water & Mold Damage Experts Painting: Interior/ Exterior Flooring: Wood / LVT / Carpet Plumbing: Repairs & Upgrades Electric: Lights & Energy Efficient Upgrades Kitchen & Bath Remodels Fast Inspections Repair Billed Thru Escrow BrightHarborBuilds.com 555-418-2796

Colors
0054AA
0677BA
7BADD7
CADEEF
E8F1F8

Requirements
Must have
• One Sided Only: #1 General Contractor for Realtors Remodels – Renovations – Repairs Water & Mold Damage Experts Painting: Interior/ Exterior Flooring: Wood / LVT / Carpet Plumbing: Repairs & Upgrades Electric: Lights & Energy Efficient Upgrades Kitchen & Bath Remodels Fast Inspections Repair Billed Thru Escrow BrightHarborBuilds.com 555-418-2796

```html
<!DOCTYPE html>
<html lang="en">
<head>
<meta charset="utf-8">
<title>General Contractor for Realtors – Business Card</title>
<link rel="stylesheet" href="https://fonts.googleapis.com/css2?family=Exo+2:wght@700;800&family=Montserrat:wght@600;700&display=swap">
<style>
  :root {
    --navy: #1a2a52;
    --orange: #f58220;
    --card: #ffffff;
    --page: #ffffff;
  }
  * { margin: 0; padding: 0; box-sizing: border-box; }
  html, body {
    width: 960px; height: 1200px; overflow: hidden;
    background: var(--page);
  }
  .business-card {
    position: absolute;
    left: 40px; top: 348px;
    width: 880px; height: 504px;
    background: var(--card);
    border-radius: 30px;
    overflow: hidden;
    box-shadow: 0 0 0 1px #eeeeee;
    font-family: "Montserrat", Arial, sans-serif;
  }
  .headline {
    position: absolute; left: 50px; top: 16px;
    font-family: "Exo 2", Arial, sans-serif;
    font-weight: 800; font-size: 27.5px; line-height: 1.1;
    color: var(--navy); letter-spacing: 0.3px;
    white-space: nowrap;
  }
  .tagline {
    position: absolute; white-space: nowrap;
    font-weight: 700; font-size: 14.5px; line-height: 1.2;
  }
  .tagline--services { left: 57px; top: 46px; color: var(--orange); letter-spacing: 6.8px; }
  .tagline--experts { left: 87px; top: 68px; color: var(--navy); letter-spacing: 7px; }
  .house-art {
    position: absolute; left: 579px; top: 46px;
    width: 251px; height: 91px;
    border-radius: 6px;
    background: linear-gradient(90deg, #d9dde6 0%, #f9c79b 50%, #d9dde6 100%);
  }
  .service-list { position: absolute; left: 50px; top: 102px; list-style: none; width: 640px; }
  .service {
    position: relative;
    height: 41px; line-height: 41px;
    font-size: 33px; font-weight: 600; white-space: nowrap;
  }
  .service__name { position: absolute; left: 0; color: var(--orange); }
  .service__colon { position: absolute; left: 166px; color: var(--orange); }
  .service__value { position: absolute; left: 184px; color: var(--navy); }
  .service--tight .service__value { left: 180px; }
  .feature {
    position: absolute; left: 50px; top: 268px;
    font-size: 42px; line-height: 50px; font-weight: 700; color: var(--orange); white-space: nowrap;
  }
  .info-line {
    position: absolute; left: 50px;
    font-size: 33px; line-height: 40px; font-weight: 600; color: var(--navy); white-space: nowrap;
  }
  .info-line--escrow { top: 319px; }
  .info-line--web { top: 359px; }
  .info-line--phone { top: 399px; font-size: 35px; color: var(--orange); font-weight: 700; }
  .color-band {
    position: absolute; left: 0; bottom: 0;
    width: 100%; height: 48px; display: flex;
  }
  .color-band__navy { width: 437px; background: var(--navy); }
  .color-band__orange { flex: 1; background: var(--orange); }
</style>
</head>
<body>
  <section class="business-card">
    <h1 class="headline">GENERAL CONTRACTOR FOR REALTORS</h1>
    <p class="tagline tagline--services">REMODELS – RENOVATIONS – REPAIRS</p>
    <p class="tagline tagline--experts">WATER &amp; MOLD DAMAGE EXPERTS</p>
    <div class="house-art" role="img" aria-label="Illustration of house rooftops with a worker and tools in navy and orange"></div>

    <ul class="service-list">
      <li class="service"><span class="service__name">Painting</span><span class="service__colon">:</span><span class="service__value">Interior/ Exterior</span></li>
      <li class="service"><span class="service__name">Flooring</span><span class="service__colon">:</span><span class="service__value">Wood / LVT / Carpet</span></li>
      <li class="service service--tight"><span class="service__name">Plumbing:</span><span class="service__value">Repairs &amp; Upgrades</span></li>
      <li class="service service--tight"><span class="service__name">Electric</span><span class="service__colon">:</span><span class="service__value">Lights &amp; Energy Efficient Upgrades</span></li>
    </ul>

    <p class="feature">Kitchen &amp; Bath Remodels</p>
    <p class="info-line info-line--escrow">Fast Inspections Repair Billed Thru Escrow</p>
    <p class="info-line info-line--web">BrightHarborBuilds.com</p>
    <p class="info-line info-line--phone">555-418-2796</p>

    <div class="color-band"><span class="color-band__navy"></span><span class="color-band__orange"></span></div>
  </section>
</body>
</html>
```